New ecommerce website needed for Epoxy Retailer

We need a new shopify website designed and built for our epoxy supply store.
We sell Epoxy, wood, epoxy furniture, supplies and provide classes on how to use epoxy.
We are looking for a website with a home page and 7 primary navigation links at the top. Some of these links should have a drop down menu with the below listed pages linked to them...
Sub Pages:
- Brindle Epoxy
- Epoxy
- Pigments
- Marten Oil
- Molds
- Silicone
- HDPE
- Wood
- Live Edge
- Ovals & Rounds
- Pre-cut
- Charcuterie Wood
- Custom Milling
- Wholesale
- Supplies
- Furniture
-Education
- In person workshops
- My courses (are we able to have a login section for customers to see their purchases?)
- About Us

```html
<!DOCTYPE html>
<html lang="en">
<head>
<meta charset="utf-8">
<title>Grainpour Studio</title>
<link href="https://fonts.googleapis.com/css2?family=Bebas+Neue&family=Pathway+Gothic+One&display=swap" rel="stylesheet">
<style>
:root{
  --ink:#1b1b1b;
  --text:#2e2e2e;
  --muted:#555;
  --line:#9a9a9a;
  --paper:#ffffff;
  --frame:#6d6d6d;
}
*{box-sizing:border-box;margin:0;padding:0}
html,body{width:1200px;height:4295px;overflow:hidden;background:var(--paper)}
body{position:relative;font-family:"Pathway Gothic One",sans-serif;color:var(--text)}
.abs{position:absolute}
.display{font-family:"Bebas Neue",sans-serif;color:var(--ink);letter-spacing:1px}
a{color:inherit;text-decoration:none}

/* header */
.site-header{left:0;top:0;width:1200px;height:90px}
.brand{left:110px;top:8px;width:76px;height:76px;border:2px solid var(--ink);border-radius:50%;display:flex;align-items:center;justify-content:center;text-align:center;font-size:13px;line-height:13px;color:var(--ink);text-transform:uppercase}
.main-nav{left:198px;top:38px;display:flex;gap:0;font-size:13px;text-transform:uppercase;color:var(--ink)}
.main-nav span{margin-right:28px}
.main-nav .drop::after{content:"";display:inline-block;width:4px;height:4px;border-right:1.3px solid var(--ink);border-bottom:1.3px solid var(--ink);transform:rotate(45deg);margin:0 0 3px 4px}
.header-icons{left:990px;top:33px;display:flex;gap:20px}

/* hero */
.hero{left:0;top:90px;width:1200px;height:612px;background:radial-gradient(ellipse at 55% 70%,#9a6a3a 0%,#6e4526 40%,#3a2516 100%)}
.hero-title{left:0;top:275px;width:1200px;text-align:center;font-size:54px;color:#fff}
.hero-btn{left:528px;top:357px;width:142px;height:45px;border:2px solid #fff;color:#fff;font-size:13px;display:flex;align-items:center;justify-content:center;text-transform:uppercase}

/* intro columns */
.col-title{font-size:34px;text-align:center}
.col-text{font-size:19.5px;line-height:27.5px;text-align:justify;text-align-last:center}

/* products */
.section-title{font-size:40px;text-align:center}
.product-img{width:239px;height:241px;border:1px solid var(--frame)}
.product-name{font-size:19px}
.price{font-size:17px;color:var(--muted)}
.price s{margin-right:28px}

.ph-frame{border:1px solid var(--frame)}
.play{left:558px;top:3176px;width:84px;height:84px;border-radius:50%;background:#fff;display:flex;align-items:center;justify-content:center}

.foot-title{font-size:24px}
.foot-list{list-style:none;font-size:16px;line-height:25.7px;text-transform:uppercase;color:var(--muted)}
.email-box{left:111px;top:4095px;width:334px;height:44px;border:1.5px solid var(--ink);font-size:15px;color:#888;padding:12px 20px}
.social{left:880px;top:4094px;display:flex;gap:12px;font-size:11px;color:var(--ink)}
.social span{display:flex;align-items:center;gap:3px}
.social i{display:inline-block;width:7px;height:7px;border-radius:50%;background:var(--ink)}
.rule{left:111px;top:4170px;width:978px;height:1px;background:var(--line)}
.payments{left:460px;top:4192px;display:flex;gap:8px}
.payments span{width:40px;height:24px;border:1px solid #ccc;border-radius:3px;font-size:9px;display:flex;align-items:center;justify-content:center;color:#333}
.copy{left:0;top:4240px;width:1200px;text-align:center;font-size:13px;color:var(--ink)}
</style>
</head>
<body>

<header class="abs site-header">
  <div class="abs brand">Grainpour<br>Studio</div>
  <nav class="abs main-nav">
    <span>Home</span><span class="drop">Products</span><span class="drop">Wholesale</span><span class="drop">Supplies</span><span class="drop">Furniture</span><span class="drop">Education</span><span class="drop">My Courses</span><span>About Us</span>
  </nav>
  <div class="abs header-icons">
    <svg width="20" height="20" viewBox="0 0 20 20" fill="none" stroke="#1b1b1b" stroke-width="2"><circle cx="8" cy="8" r="6"/><path d="M12.5 12.5l6 6"/></svg>
    <svg width="20" height="20" viewBox="0 0 20 20" fill="none" stroke="#1b1b1b" stroke-width="1.6"><circle cx="10" cy="7" r="4"/><path d="M3 18c1-4 4-5 7-5s6 1 7 5z"/></svg>
    <svg width="20" height="20" viewBox="0 0 20 20" fill="none" stroke="#1b1b1b" stroke-width="1.6"><rect x="3" y="6" width="14" height="12" rx="1"/><path d="M7 6a3 3 0 0 1 6 0"/></svg>
  </div>
</header>

<section class="abs hero" role="img" aria-label="Craftsman pouring dark resin over a live edge wooden slab in a workshop"></section>
<h1 class="abs display hero-title">Grainpour Studio</h1>
<a class="abs hero-btn">Shop Now</a>

<h2 class="abs display col-title" style="left:115px;top:762px;width:430px">About Us</h2>
<p class="abs col-text" style="left:115px;top:815px;width:430px">Saerspiciatis unde omnis iste natus error sit voluptatem accusantium doloremque laudantium, totam rem aperiam, eaque ipsa quae ab illo inventore veritatis et quasi architecto beatae vitae dicta sunt explicabo. Nemo enim ipsam voluptatem quia voluptas sit aspernatur aut odit aut fugit, sed quia consequuntur magni dolores.</p>
<h2 class="abs display col-title" style="left:658px;top:762px;width:430px">Education</h2>
<p class="abs col-text" style="left:658px;top:815px;width:430px">Saerspiciatis unde omnis iste natus error sit voluptatem accusantium doloremque laudantium, totam rem aperiam, eaque ipsa quae ab illo inventore veritatis et quasi architecto beatae vitae dicta sunt explicabo. Nemo enim ipsam voluptatem quia voluptas sit aspernatur aut odit aut fugit, sed quia consequuntur magni dolores.</p>

<h2 class="abs display section-title" style="left:0;top:1064px;width:1235px">Our Products</h2>
<p class="abs" style="left:300px;top:1120px;width:600px;text-align:center;font-size:18px;line-height:27px">Saersp iciatisunde omnisiste natus errorsit voluptatem accusantium doloremque laudanti umtotamrem aperiameaque ipsa quae ab illo</p>

<div class="abs product-img" style="left:111px;top:1205px;background:linear-gradient(160deg,#e9e4df 0%,#b38d6d 40%,#6b2f8a 75%,#3c1d5a 100%)" role="img" aria-label="Resin being poured into a wood river table mould"></div>
<div class="abs product-img" style="left:358px;top:1205px;background:radial-gradient(circle at 50% 70%,#9ec8e6 0%,#1d6fb5 35%,#0c2236 100%)" role="img" aria-label="Gloved hand pouring clear epoxy from a cup"></div>
<div class="abs product-img" style="left:604px;top:1205px;background:radial-gradient(circle at 50% 50%,#e2c43a 0%,#c63a3a 25%,#3a4fbf 40%,#ffffff 65%)" role="img" aria-label="Piles of yellow, red and blue pigment powder"></div>
<div class="abs product-img" style="left:851px;top:1205px;background:radial-gradient(circle at 50% 48%,#e8b83a 0%,#f3dc8c 25%,#ffffff 55%)" role="img" aria-label="Golden oil droplet splash"></div>

<div class="abs product-name display" style="left:112px;top:1462px">Brindle Epoxy</div>
<div class="abs product-name display" style="left:359px;top:1462px">Epoxy</div>
<div class="abs product-name display" style="left:605px;top:1462px">Pigments</div>
<div class="abs product-name display" style="left:852px;top:1462px">Marten Oil</div>
<div class="abs price" style="left:112px;top:1495px"><s>$ 457.00</s>From $ 400.00</div>
<div class="abs price" style="left:359px;top:1495px"><s>$ 457.00</s>From $ 400.00</div>
<div class="abs price" style="left:605px;top:1495px"><s>$ 457.00</s>From $ 400.00</div>
<div class="abs price" style="left:852px;top:1495px"><s>$ 457.00</s>From $ 400.00</div>

<div class="abs product-img" style="left:111px;top:1556px;background:radial-gradient(circle at 45% 50%,#8fd23a 0%,#2fa0c8 25%,#f07a3a 40%,#ffffff 60%)" role="img" aria-label="Stack of colourful silicone cupcake moulds"></div>
<div class="abs product-img" style="left:358px;top:1556px;background:linear-gradient(135deg,#f2d23a 0%,#ef5fa8 35%,#3ab7e0 65%,#f08a3a 100%)" role="img" aria-label="Assorted bright silicone baking tools"></div>
<div class="abs product-img" style="left:604px;top:1556px;background:linear-gradient(135deg,#7a4e2c 0%,#a9774a 50%,#5c3a20 100%)" role="img" aria-label="Wall of square wooden blocks"></div>
<div class="abs product-img" style="left:851px;top:1556px;background:radial-gradient(circle at 50% 50%,#ffffff 40%,#e6d29a 70%,#ffffff 100%)" role="img" aria-label="Gold oval and square frames"></div>

<div class="abs product-name display" style="left:112px;top:1813px">Molds</div>
<div class="abs product-name display" style="left:359px;top:1813px">Silicone</div>
<div class="abs product-name display" style="left:605px;top:1813px">Wood</div>
<div class="abs product-name display" style="left:852px;top:1813px">Ovals &amp; Rounds</div>
<div class="abs price" style="left:112px;top:1846px"><s>$ 457.00</s>From $ 400.00</div>
<div class="abs price" style="left:359px;top:1846px"><s>$ 457.00</s>From $ 400.00</div>
<div class="abs price" style="left:605px;top:1846px"><s>$ 457.00</s>From $ 400.00</div>
<div class="abs price" style="left:852px;top:1846px"><s>$ 457.00</s>From $ 400.00</div>

<h2 class="abs display" style="left:111px;top:1988px;font-size:42px">Wholesale</h2>
<div class="abs ph-frame" style="left:111px;top:2067px;width:647px;height:723px;background:linear-gradient(150deg,#cfa47a 0%,#2c8fd0 25%,#6a2f9a 55%,#1a5fc0 80%,#c99a6e 100%)" role="img" aria-label="Blue and purple resin poured into a clamped wood river table"></div>
<div class="abs ph-frame" style="left:766px;top:2067px;width:323px;height:318px;background:radial-gradient(circle at 40% 60%,#c89a64 0%,#6a4a2e 45%,#5b7a3a 100%)" role="img" aria-label="Stack of cut logs"></div>
<div class="abs product-name display" style="left:766px;top:2392px">Pre-cut</div>
<div class="abs price" style="left:766px;top:2425px">From $ 400.00</div>
<div class="abs ph-frame" style="left:766px;top:2473px;width:323px;height:317px;background:linear-gradient(180deg,#4a3020 0%,#6e4a30 40%,#3a2418 100%)" role="img" aria-label="Rustic reclaimed wood planks"></div>
<div class="abs product-name display" style="left:111px;top:2806px">Epoxy</div>
<div class="abs product-name display" style="left:766px;top:2806px">Charcuterie Wood</div>

<div class="abs ph-frame" style="left:111px;top:2963px;width:978px;height:509px;background:linear-gradient(160deg,#ebe6e0 0%,#f4f4f4 30%,#1f6fd6 50%,#c9a27c 70%,#8d6445 100%)" role="img" aria-label="Video of blue resin being poured into a wood table mould"></div>
<div class="abs play"><svg width="24" height="26" viewBox="0 0 24 26"><path d="M4 2l18 11-18 11z" fill="#1b1b1b"/></svg></div>

<h2 class="abs display col-title" style="left:115px;top:3565px;width:430px">My Courses</h2>
<p class="abs col-text" style="left:115px;top:3618px;width:430px">Saerspiciatis unde omnis iste natus error sit voluptatem accusantium doloremque laudantium, totam rem aperiam, eaque ipsa quae ab illo inventore veritatis.</p>
<h2 class="abs display col-title" style="left:658px;top:3565px;width:430px">Wholesale</h2>
<p class="abs col-text" style="left:658px;top:3618px;width:430px">Uasepeserspiciatis unde omnis iste natus error sit voluptatem accusantium doloremque laudantium, totam rem aperiam, eaque ipsa quae ab.</p>

<footer>
  <h3 class="abs display foot-title" style="left:121px;top:3786px">Quick Links</h3>
  <ul class="abs foot-list" style="left:121px;top:3830px"><li>Home</li><li>Products</li><li>Wholesale</li><li>Supplies</li><li>Furniture</li><li>Education</li><li>My Courses</li></ul>
  <h3 class="abs display foot-title" style="left:470px;top:3786px">Links</h3>
  <ul class="abs foot-list" style="left:470px;top:3830px"><li>Copyright</li><li>About Us</li><li>Legal</li><li>Privacy</li><li>Accessibility</li><li>Sitemap</li></ul>
  <h3 class="abs display foot-title" style="left:674px;top:3786px">Our Mission</h3>
  <p class="abs col-text" style="left:674px;top:3822px;width:428px;text-align-last:left">Saerspiciatis unde omnis iste natus error sit voluptatem accusantium doloremque laudantium, totam rem aperiam, eaque ipsa quae abillo</p>

  <h3 class="abs display" style="left:111px;top:4055px;font-size:20px">Subscribe to our emails</h3>
  <div class="abs email-box">Email</div>
  <svg class="abs" style="left:407px;top:4109px" width="20" height="16" viewBox="0 0 20 16" fill="none" stroke="#1b1b1b" stroke-width="1.6"><path d="M1 8h17M12 2l6 6-6 6"/></svg>

  <div class="abs social"><span><i></i>Chirrup</span><span><i></i>Pagebook</span><span><i></i>Snapframe</span><span><i></i>Tiktune</span><span><i></i>Vidstream</span></div>

  <div class="abs rule"></div>
  <div class="abs payments"><span>Veyra</span><span>Circlepay</span><span>Amerocard</span><span>Paywell</span><span>Dinerly</span><span>Findcard</span></div>
  <p class="abs copy">©2022. All rights reserved.</p>
</footer>

</body>
</html>
```